Flyer Design Project

I need to create a flyer to advertise an Luxury Self Catering Apartment Complex in a Ski Resort in Europe. The development offers luxury accommodation to those who are on a budget.

Below is what needs to be included and a basic layout design idea i had that can be changed. The information is important. Hoping to get it on a flyer sized 21.6 x 14 cm

Title - 'Luxury Self Catering Ski Apartments For Rent'
Sub Title - 'Located 200m from Gondola, Restaurants and Bars'

Studio - Sleeps 1-2 - From only £200 per week
1 Bed - Sleeps 2-4 - From only £250 per week
2 Bed - Sleeps 4-6 - From only £350 per week

Image 1 Image 2 Image 3

- Fully Furnished Modern, Spacious & Comfortable Apartments
- Fully Staffed Development (Reception, Bar + Daily Cleaning)
- Family friendly & suitable for children of all ages

(Twitter Icon) @snowlarkchalets
E-mail - snowlarkchalets@mailvora.co.uk
Telephone - +44 (0) 7811 302 684

Target Market(s)

Our target market is very wide. We are trying to attract students, couples and families who are skiing on a budget.

Industry/Entity Type

Accommodation

Requirements
Must have
• The text contained in 'task description' is important but i'd like to be led on design. Size of around 21.6 x 14cm is important and i'd like the 3 images below (hopefully someone can get of the date and time in orange bottom right of all pics)

http://i2217.picvaultra.com/albums/kq412/tmwimages/Bansko/699_00_640_zpsd7b2ba81.jpeg

http://i2217.picvaultra.com/albums/kq412/tmwimages/Bansko/a_02_zps7503dd10.jpeg

http://i2217.picvaultra.com/albums/kq412/tmwimages/Bansko/699_08_640_zps2f11bf21.jpeg

```html
<!DOCTYPE html>
<html lang="en">
<head>
<meta charset="utf-8">
<title>Luxury Self Catering Ski Apartments For Rent</title>
<link rel="stylesheet" href="https://fonts.googleapis.com/css2?family=Arimo:wght@700&family=Libre+Baskerville:wght@700&family=Tinos:wght@400;700&display=swap">
<style>
  :root {
    --blue-deep: #143f8f;
    --blue-mid: #2a5fb6;
    --blue-light: #4f86d0;
    --snow: #ffffff;
    --ink: #111111;
    --red: #e3251b;
    --lavender: #e9e9f6;
    --info-box: #a9d0ef;
    --navy-text: #12305f;
    --footer-text: #1d2b4a;
  }
  * { margin: 0; padding: 0; box-sizing: border-box; }
  html, body { width: 778px; height: 1200px; overflow: hidden; background: #ffffff; }
  .flyer {
    position: relative;
    width: 778px;
    height: 1200px;
    overflow: hidden;
    background: radial-gradient(ellipse at 80% 30%, var(--blue-light) 0%, var(--blue-mid) 40%, var(--blue-deep) 100%);
    font-family: "Arimo", Arial, sans-serif;
  }
  .ski-scene { position: absolute; left: 0; top: 0; width: 778px; height: 900px; }
  .headline {
    position: absolute;
    left: 250px; top: 22px; width: 520px;
    text-align: center;
    color: var(--snow);
    font-family: "Libre Baskerville", Georgia, serif;
    font-weight: 700;
    font-size: 32px;
    line-height: 1.3;
    text-shadow: 1px 2px 3px rgba(0,0,0,0.35);
  }
  .location-banner {
    position: absolute;
    left: 435px; top: 153px; width: 330px; height: 52px;
    background: var(--lavender);
    color: var(--red);
    font-family: "Libre Baskerville", Georgia, serif;
    font-weight: 700;
    font-variant: small-caps;
    font-size: 18px;
    line-height: 23px;
    text-align: center;
    padding-top: 3px;
  }
  .room-photo {
    position: absolute;
    border-radius: 50%;
    border: 4px solid var(--snow);
    box-shadow: 0 2px 8px rgba(0,0,0,0.35);
  }
  .room-photo--living { left: 450px; top: 252px; width: 150px; height: 150px;
    background: radial-gradient(circle at 40% 45%, #d8c3a2, #8a6a48 70%, #4b3a2a); }
  .room-photo--kitchen { left: 494px; top: 400px; width: 266px; height: 266px;
    background: radial-gradient(circle at 45% 50%, #6b5238, #3a2b1f 60%, #b7a58d); }
  .room-photo--bedroom { left: 376px; top: 556px; width: 220px; height: 220px;
    background: radial-gradient(circle at 45% 55%, #f1e7d6, #c9a27a 55%, #8b5a38); }
  .apartment { position: absolute; color: var(--ink); font-weight: 700; font-size: 20px; line-height: 25px; }
  .apartment__name {
    color: var(--red);
    font-family: "Libre Baskerville", Georgia, serif;
    font-size: 27px;
    line-height: 1;
    margin-bottom: 26px;
  }
  .apartment--studio { left: 40px; top: 448px; }
  .apartment--studio .apartment__name { margin-left: 54px; }
  .apartment--single { left: 64px; top: 590px; }
  .apartment--single .apartment__name { margin-left: 46px; margin-bottom: 28px; }
  .apartment--double { left: 84px; top: 757px; }
  .apartment--double .apartment__name { margin-left: 86px; margin-bottom: 20px; }
  .features {
    position: absolute;
    left: 161px; top: 898px; width: 568px; height: 176px;
    background: var(--info-box);
    box-shadow: 0 2px 6px rgba(0,0,0,0.25);
    padding: 22px 24px;
    color: var(--navy-text);
    font-weight: 700;
    font-size: 19px;
    line-height: 25px;
    list-style: none;
  }
  .features li + li { margin-top: 8px; }
  .contact-bar {
    position: absolute;
    left: 0; top: 1127px; width: 778px; height: 73px;
    background: var(--snow);
    display: flex; align-items: center;
    padding-left: 24px;
    font-family: "Tinos", "Times New Roman", serif;
    font-size: 15px;
    color: var(--footer-text);
  }
  .contact-bar__social { display: flex; align-items: center; gap: 8px; width: 250px; }
  .contact-bar__marker { width: 26px; height: 26px; border-radius: 4px; background: #3aa4e8; }
  .contact-bar__email { width: 330px; }
</style>
</head>
<body>
<div class="flyer">
  <svg class="ski-scene" viewBox="0 0 778 900" xmlns="http://www.w3.org/2000/svg" role="img" aria-label="Photograph of a skier carving down a snowy slope">
    <defs>
      <linearGradient id="snowTone" x1="0" y1="0" x2="1" y2="1">
        <stop offset="0" stop-color="#ffffff"/>
        <stop offset="0.6" stop-color="#f3f6fb"/>
        <stop offset="1" stop-color="#d3e0f2"/>
      </linearGradient>
    </defs>
    <path d="M0,0 L230,0 C320,160 380,330 385,480 C390,640 340,790 260,900 L0,900 Z" fill="url(#snowTone)"/>
  </svg>

  <h1 class="headline">Luxury Self Catering Ski<br>Apartments For Rent</h1>
  <p class="location-banner">Located 200m from Gondola,<br>Restaurants and Bars</p>

  <div class="room-photo room-photo--living" role="img" aria-label="Photograph of the apartment living area with sofa"></div>
  <div class="room-photo room-photo--kitchen" role="img" aria-label="Photograph of the open kitchen and dining area"></div>
  <div class="room-photo room-photo--bedroom" role="img" aria-label="Photograph of a double bedroom"></div>

  <section class="apartment apartment--studio">
    <h2 class="apartment__name">Studio</h2>
    <p>Sleeps 1-2 people</p>
    <p>Price: £ 200 per week</p>
  </section>
  <section class="apartment apartment--single">
    <h2 class="apartment__name">Single Bed</h2>
    <p>Sleeps 2-4 people</p>
    <p>Price: £ 250 per week</p>
  </section>
  <section class="apartment apartment--double">
    <h2 class="apartment__name">Double Bed</h2>
    <p>Sleeps 4-6 people</p>
    <p>Price: £ 350 per week</p>
  </section>

  <ul class="features">
    <li>- Fully furnished Modern, Spacious &amp; Comfortable</li>
    <li>- Fully stuffed Development<br>&nbsp;&nbsp;(Reception, Bar &amp; Daily cleaning)</li>
    <li>- Family friendly &amp; Suitable for children of all ages</li>
  </ul>

  <footer class="contact-bar">
    <span class="contact-bar__social"><span class="contact-bar__marker"></span>@snowlarkchalets</span>
    <span class="contact-bar__email">E-mail: snowlarkchalets@mailvora.co.uk</span>
    <span class="contact-bar__phone">Tel: +44(0) 7811 302 684</span>
  </footer>
</div>
</body>
</html>
```